Zielgruppe
Unsere Firma produziert individuelles Büromaterialen aus Papier & Kunststoff (bspw. Ringbücher, Klarsichthüllen, Mappen, etc.) Zielgruppe sind (eher konservative) Unternehmenskunden in allen Branchen (speziell Logistik, KFZ, Gesundheit).
Die Broschüre soll primär zur Neukundenakquise als auch für Neuverkäufe an Bestandskunden verwendet werden und in einem schlichten, modernen und hochwertigen Design eine Übersicht über unser Produktportfolio bieten.
Aufgabenstellung
Die Broschüre soll auf Basis des bestehenden Corporate Designs gestaltet werden.
1) In der Broschüre soll jede unserer fünf Produktkategorien (Ordner, Ringbuchordner, Ordnerregister, Hüllen & Taschen, Mappen) eine eigene Seite/Abschnitt erhalten, ähnlich unserer Website.
2) Zudem soll auf einer eigenen Seite/Abschnitt prägnant darauf hingewiesen werden, dass wir für alle Produktkategorie individuelle Sonderanfertigungen anbieten.
Die Strukturierung und Aufteilung der Inhalt in der Broschüre soll sich relativ klar an unserer Website orientieren. Medien & bereits vorhandene Texte sind sowohl als Anlage dem Projekt beigefügt, als auch auf unserer Website auffindbar. Falls notwendig wären wir auch bereit zu einzelnen Themenbereiche neue Texte erstellen zu lassen.
Hinsichtlich des Formats überlassen wir die Auswahl dem Designer. Die Broschüre wird jedoch auch häufig in digitaler Form versandt.

```html
<!DOCTYPE html>
<html lang="de">
<head>
<meta charset="utf-8">
<title>Broschüre – Über uns / Ordner</title>
<link rel="stylesheet" href="https://fonts.googleapis.com/css2?family=Orbitron:wght@400;500&family=Arimo:ital,wght@0,400;0,700;1,700&display=swap">
<style>
  :root {
    --backdrop: #8a939c;
    --paper: #f7f7f8;
    --brand-blue: #1f3f8e;
    --brand-blue-dark: #17337a;
    --soft-blue: #dde3ef;
    --tag-blue: #b3bfda;
    --ink: #2a2d33;
    --photo-building-top: #8d9a6d;
    --photo-building-bottom: #a3a49c;
    --photo-ring-top: #c7bba8;
    --photo-ring-bottom: #e9e7e2;
    --photo-binder-top: #cdbba2;
    --photo-binder-bottom: #a88c70;
  }
  * { margin: 0; padding: 0; box-sizing: border-box; }
  html, body { width: 1200px; height: 960px; overflow: hidden; }
  body {
    background: var(--backdrop);
    font-family: "Arimo", Arial, sans-serif;
    color: var(--ink);
  }
  .spread {
    position: absolute;
    left: 60px; top: 98px;
    width: 1080px; height: 764px;
    display: flex;
  }
  .page {
    position: relative;
    width: 540px; height: 764px;
    background: var(--paper);
    overflow: hidden;
  }
  .page--left { box-shadow: inset -18px 0 24px -20px rgba(0,0,0,.25); }
  .page--right { box-shadow: inset 18px 0 24px -20px rgba(0,0,0,.25); }
  .page-art { position: absolute; inset: 0; }

  .heading {
    font-family: "Orbitron", sans-serif;
    font-weight: 400;
    color: var(--brand-blue);
    letter-spacing: 1px;
    position: absolute;
  }
  .subheading {
    font-family: "Orbitron", sans-serif;
    color: var(--ink);
    letter-spacing: 1.5px;
    position: absolute;
  }
  .tagline {
    position: absolute;
    font-weight: 700;
    color: var(--tag-blue);
    font-size: 9px;
  }
  .body-copy {
    position: absolute;
    font-size: 8.6px;
    line-height: 1.32;
  }
  .body-copy p + p { margin-top: 6px; }
  .body-copy .lead-word { color: var(--tag-blue); font-weight: 700; }
  .body-copy--justified p { text-align: justify; }

  /* left page */
  .about-title { left: 40px; top: 392px; font-size: 36px; }
  .about-company { left: 42px; top: 440px; font-size: 15px; }
  .about-tagline { left: 42px; top: 478px; }
  .about-col-1 { left: 42px; top: 500px; width: 210px; }
  .about-col-2 { left: 276px; top: 500px; width: 220px; }

  /* right page */
  .section-title { left: 40px; top: 70px; font-size: 34px; }
  .section-sub { left: 42px; top: 118px; font-size: 14px; }
  .section-label {
    position: absolute; right: 30px; top: 104px;
    font-family: "Orbitron", sans-serif; font-size: 10px; letter-spacing: 1.5px;
  }
  .highlights {
    position: absolute; left: 54px; top: 166px; width: 420px;
    list-style: none;
    font-size: 10.5px; font-weight: 700; font-style: italic;
    color: var(--brand-blue); line-height: 1.45;
  }
  .highlights li::before { content: "▪"; margin-right: 6px; font-style: normal; font-size: 8px; }
  .ordner-tagline { left: 40px; top: 480px; }
  .ordner-copy { left: 40px; top: 500px; width: 468px; }
</style>
</head>
<body>
<main class="spread">
  <!-- left page: about -->
  <section class="page page--left">
    <svg class="page-art" width="540" height="764" viewBox="0 0 540 764">
      <defs>
        <linearGradient id="building-tones" x1="0" y1="0" x2="0" y2="1">
          <stop offset="0" stop-color="var(--photo-building-top)"/>
          <stop offset="1" stop-color="var(--photo-building-bottom)"/>
        </linearGradient>
        <linearGradient id="band-fade" x1="0" y1="0" x2="1" y2="0">
          <stop offset="0" stop-color="var(--brand-blue-dark)"/>
          <stop offset="1" stop-color="#4a66a8"/>
        </linearGradient>
      </defs>
      <path role="img" aria-label="Luftaufnahme des Firmengebäudes mit Flachdach, Parkplatz und Waldrand"
            d="M40 30 H505 V450 Q300 360 40 348 Z" fill="url(#building-tones)"/>
      <path d="M220 362 Q400 380 505 450 L505 466 Q390 396 220 374 Z" fill="url(#band-fade)"/>
    </svg>
    <h1 class="heading about-title">Über uns</h1>
    <h2 class="subheading about-company">Falkner Kunststoff UG</h2>
    <p class="tagline about-tagline">Ordnung. Präsentation. Gestaltung.</p>
    <div class="body-copy about-col-1">
      <p>Falkner Kunststoff steht für individuelle Lösungen für Ordnung und Präsentation.</p>
      <p><span class="lead-word">Ordnung</span> schaffen wir für Sie mit unseren maßgefertigten Produkten zur strukturierten Ablage im Büro-, Produktions-, sowie Logistikbereich. Mit unseren Produkten gelingt die strukturierte und effiziente Ablage in allen Szenarien.</p>
      <p>Die Präsentation Ihrer Marke ermöglichen wir mit unseren individuell gefertigten und bedruckten Ringbüchern, Ringbuchordnern und Mappen. So gelingt die perfekte Kundenpräsentation verbunden mit einem repräsentativen Auftritt.</p>
    </div>
    <div class="body-copy body-copy--justified about-col-2">
      <p>Als Spezialist für Sonderanfertigungen freuen wir uns bei der Gestaltung der Produkte jedem Kunden individuelle Angebote für seinen Anwendungsfall zu erstellen. Dadurch erhalten Sie bei uns nicht bloß einzelne Produkte, sondern ein vollständiges Konzept – Von der Produktgestaltung bis hin zum Layout.</p>
      <p>Unsere Produkte zeichnen sich durch höchste Qualität – Made in Germany – Haltbarkeit und Recyclingfähigkeit aus. Durch unseren langjährigen Erfahrungsschatz können wir jedem Kunden eine individuelle Anpassung unserer Produkte anbieten. Von der technischen Produktgestaltung bis hin zur Layouterstellung erhalten Sie bei uns alles aus einer Hand. Dabei bieten wir gerne auch Kleinauflagen an.</p>
    </div>
  </section>

  <!-- right page: Ordner -->
  <section class="page page--right">
    <svg class="page-art" width="540" height="764" viewBox="0 0 540 764">
      <defs>
        <linearGradient id="ring-tones" x1="0" y1="0" x2="0" y2="1">
          <stop offset="0" stop-color="var(--photo-ring-top)"/>
          <stop offset="1" stop-color="var(--photo-ring-bottom)"/>
        </linearGradient>
        <linearGradient id="binder-tones" x1="0" y1="0" x2="0" y2="1">
          <stop offset="0" stop-color="var(--photo-binder-top)"/>
          <stop offset="1" stop-color="var(--photo-binder-bottom)"/>
        </linearGradient>
      </defs>
      <line x1="300" y1="96" x2="540" y2="96" stroke="var(--brand-blue)" stroke-width="3"/>
      <rect x="30" y="156" width="450" height="72" fill="var(--soft-blue)"/>
      <path d="M30 156 H50 L38 228 H30 Z" fill="var(--brand-blue)"/>
      <rect role="img" aria-label="Foto: geöffneter Ordner mit Ringmechanik auf Holztisch"
            x="40" y="250" width="236" height="196" fill="url(#ring-tones)"/>
      <rect role="img" aria-label="Foto: bedruckter Ordner stehend auf Holzboden"
            x="288" y="262" width="222" height="210" fill="url(#binder-tones)"/>
    </svg>
    <h1 class="heading section-title">Ordner</h1>
    <h2 class="subheading section-sub">Ordner bedruckt.</h2>
    <span class="section-label">ORDNER</span>
    <ul class="highlights">
      <li>100% individuelles Ordner-Design. Bedruckt nach Ihren Wünschen.</li>
      <li>Vollflächiger Druck möglich. Außen &amp; innen!</li>
      <li>Hochwertige Druckqualität durch modernsten Digitaldruck</li>
      <li>Mehr als 60 Jahre Erfahrung</li>
    </ul>
    <p class="tagline ordner-tagline">Mit individuellem Aufdruck werden Aktenordner zum Aushängeschild</p>
    <div class="body-copy body-copy--justified ordner-copy">
      <p>Schon in der Bezeichnung kommt der funktionale Zweck von Ordnern zum Ausdruck: Dokumente, Rechnungen, Produktinformationen und mehr lassen sich hier geordnet abheften. So herrscht Ordnung im Büro, Lager oder in der Produktion und dank einer Beschriftung der Ordner sind Unterlagen schnell gefunden. Individuelle Ordner mit einprägsamem Aufdruck übernehmen zudem eine zusätzliche Rolle, die über den funktionalen Aspekt hinausgeht: Sie vermitteln dezent eine Werbebotschaft und tragen als Aushängeschild dazu bei, Ihr Unternehmen und Ihre Marke stilvoll zu präsentieren. Exklusiv und hochwertig, ein Ordner-Design dieser Art bleibt beispielsweise nach einer Produktvorstellung beim Gesprächspartner im Gedächtnis. Bei uns erhalten Sie qualitative und einzigartige Ordner inkl. Druck und Layout Erstellung. Ob Firmenmotto, Logo oder eine Farbgestaltung mit Wiedererkennungseffekt, wir gestalten Ihre Aktenordner exakt nach Ihren Vorgaben. Profitieren Sie von unserer Kreativität und nutzen Sie unsere Kompetenz in puncto moderner Drucktechnik.</p>
      <p>Vollflächig oder nur teilweise bedruckt, beides ist möglich. Auf Wunsch bedrucken wir individuelle Ordner auch auf der Innenseite. Dank hochwertigem Digitaldruck entsteht ein Design mit brillanter Optik. Als Unikat unterstützen die Ordner in bedruckter Ausführung das Alleinstellungsmerkmal Ihres Unternehmens. Auch die Mitarbeiter in den verschiedenen Teams wissen ansprechend gestaltete Ordner zu schätzen. Bei unseren Produkten achten wir ebenso auf eine hohe Qualität: So sind die Ordner stabil und langlebig. Gerne beraten wir Sie hinsichtlich der Gestaltung sowie des Layouts und übermitteln Ihnen ein umfassendes Konzept, das genau auf Ihren Bedarf und Ihre Zielsetzung abgestimmt ist. Machen Sie von der einfachen Möglichkeit einer Anfrage Gebrauch und zögern Sie auch nicht, wenn es sich um eine Kleinauflage handelt.</p>
    </div>
  </section>
</main>
</body>
</html>
```